Holiday Graphic for Cover of Catalog

We're looking for a design that represents the Holiday season to use on the cover of this year's holiday catalog. You can take a look at 2011's catalog at this link: http://paglerow.com/tindlecrest/docs/holiday_gift_guide. Your design should not be a replication, but it can be inspired by the cover of 2011's Catalog.

Please create a design that is WINTER-specific, not necessarily Christmas, Hanukkah, or any other holiday-specific design. Something simple, modern, contemporary is preferable. The design should have a specific color scheme & that scheme should be easily detectable by a viewer.

Options for The final size of the front-cover:
a. 8.5"width x 5.405"height
b. 8.5"width x 10.81"height
c. 10.81"height x 8.5"width
d. square 8.5" x 8.5"

Please note: I do not have the time or budget to have these printed with foil stamping, so please avoid any metallic finishes.  

Thanks!
Rosa

Requirements
Must have
• Our logo, attached file.
• Title: "2013 Holiday Gift Giving Guide"

```html
<!DOCTYPE html>
<html lang="en">
<head>
<meta charset="utf-8">
<title>2013 Holiday Gift Giving Guide</title>
<link rel="stylesheet" href="https://fonts.googleapis.com/css2?family=Bodoni+Moda:wght@400&display=swap">
<style>
  :root {
    --paper: #ffffff;
    --holly-red: #fa0000;
    --rose-pink: #ff4aa0;
    --ice-cyan: #21f0f0;
    --frost: #e9fdfd;
  }
  html, body {
    margin: 0;
    padding: 0;
    width: 1200px;
    height: 983px;
    overflow: hidden;
    background: var(--paper);
  }
  .cover {
    display: block;
    width: 1200px;
    height: 983px;
  }
  .year-digit,
  .title-main,
  .title-sub {
    font-family: "Bodoni Moda", "Didot", serif;
    font-weight: 400;
  }
  .year-digit { font-size: 205px; text-anchor: middle; }
  .year-digit--ink { fill: var(--holly-red); }
  .year-digit--knockout { fill: var(--paper); }
  .title-main { font-size: 96px; fill: var(--paper); }
  .title-sub { font-size: 40px; fill: var(--paper); }
  .swoop { fill: var(--holly-red); }
  .accent { fill: var(--rose-pink); }
</style>
</head>
<body>
<svg class="cover" viewBox="0 0 975 800" width="1200" height="983" preserveAspectRatio="none" xmlns="http://www.w3.org/2000/svg">
  <defs>
    <path id="swoop-shape" d="M410,10 L825,10 L825,140 C760,300 660,560 610,790 L522,790 C500,640 420,520 330,400 C280,320 245,240 250,180 C255,110 320,40 410,10 Z"/>
    <clipPath id="swoop-clip"><use href="#swoop-shape"/></clipPath>
    <radialGradient id="frost-glow" cx="50%" cy="50%" r="50%">
      <stop offset="0%" stop-color="var(--paper)"/>
      <stop offset="70%" stop-color="var(--frost)"/>
      <stop offset="100%" stop-color="#c8f7f7"/>
    </radialGradient>
  </defs>

  <!-- pink accents -->
  <polygon class="accent" points="213,10 266,10 213,92"/>
  <polygon class="accent" points="213,620 213,790 322,790"/>

  <!-- red swoop -->
  <use class="swoop" href="#swoop-shape"/>
  <path class="swoop" d="M380,790 C392,750 405,725 418,722 C438,735 452,765 462,790 Z"/>

  <!-- pink edge along swoop -->
  <polygon class="accent" points="300,55 256,150 252,205 262,232 305,330 318,322 268,210 266,160"/>

  <!-- year, stacked -->
  <g class="year">
    <text class="year-digit year-digit--ink" x="270" y="168">2</text>
    <text class="year-digit year-digit--ink" x="270" y="368">0</text>
    <text class="year-digit year-digit--ink" x="270" y="575">1</text>
    <text class="year-digit year-digit--ink" x="270" y="778">3</text>
    <g clip-path="url(#swoop-clip)">
      <text class="year-digit year-digit--knockout" x="270" y="168">2</text>
      <text class="year-digit year-digit--knockout" x="270" y="368">0</text>
      <text class="year-digit year-digit--knockout" x="270" y="575">1</text>
      <text class="year-digit year-digit--knockout" x="270" y="778">3</text>
    </g>
  </g>

  <!-- title -->
  <text class="title-main" x="428" y="100">Holiday</text>
  <text class="title-sub" x="428" y="158">Gift Giving Guide</text>

  <!-- snowflake artwork area -->
  <circle class="snowflake-art" cx="702" cy="512" r="248" fill="url(#frost-glow)" stroke="var(--ice-cyan)" stroke-width="1.5" role="img" aria-label="Large white and cyan snowflake illustration with a red star at its centre"/>
</svg>
</body>
</html>
```